Application for baby milk and water counter

We are building baby food app. Need to design main screen for tha app first so we can go forward to other secondary screens of the app

Food dashboard screen
Food dashboard screen is main page for view/edit food data

General vision
I see the app in pastel colors with some illustrations to make the app more in positive. You can influence from game Lantern Orchard. I see with smooth colors and gradients like in a game. Also need to have animations/transitions for each action. Each click should create smooth transition to new state. My idea is to build one dashboard screen for food which we can reuse it for other screens. So a lot of thinking should go into design stage to app appealing.

Food Dashboard
Current screen should show all the data about food intake of the baby. So here user should see

Milk How much food baby had in ml/oz. So there should be some kind of illustrated bottle or glass or smth that shows it is filled with that amount.

Add/Remove controls for food. Should be some kind of custom control for inputing amount to remove/add. I see it as a slider on the side of the bottle. User slides up or down and amount is added/removed.

Notification. So user should be aware how many hours/minutes left for next food intake. This is optional field, so consider it could be disabled. So no empty space should be on a screen. There should be human readable text. Something like. 1:30 minutes left for next intake. Maybe could be some custom made icons to illustrate that it is next food intake.

Burped: User should have ability to how much baby burped. This amount is integer value. So it could be “Baby burped 2 times today”. So again here I see some custom made/icon to illustrate how many times baby burped and amount next to it. I see changing the value just by tapping, but I don’t know how to edit if user tapped accidentally more than it should be. So TBD here.

Date and time: Dashboard should show for which date it is viewing/editing data. Should be able to change it, so user can add/edit data for yesterday. Don’t want to see here calendar on a screen so need to come up with nice design decision.

Water: User should have ability to view/edit water intake of the baby, but water is secondary information so it should be smaller than milk, or come up with some other idea how to show the water. I see to have same controls for water like for milk. Water intake is optional it can be disabled by the user.

Target Market(s)

For just became mothers

Font styles to use
Sans Serif

Colors
0094D4
00A9DD
6FCCEA
C7EBF8
E9F6FB
FFC000
F8CF3A
FAE287
FDF2CF
FEFAEE
E54698
E96AAD
F1A4CE
F9D9EA
FCEFF6

Requirements
Must have
• Ilustrations or playfull icons for show information

```html
<!DOCTYPE html>
<html lang="en">
<head>
<meta charset="utf-8">
<title>Food Dashboard</title>
<link href="https://fonts.googleapis.com/css2?family=Plus+Jakarta+Sans:wght@400;500;600;700;800&display=swap" rel="stylesheet">
<style>
  :root {
    --bg-top: #d5b8f3;
    --card: #e7d0fa;
    --panel: #f3e3fb;
    --plum: #6a2a6c;
    --ink: #3b2f45;
    --rule: #2e2436;
    --tag: #f3c6de;
    --avatar: #f9b51d;
  }
  * { margin: 0; padding: 0; box-sizing: border-box; }
  html, body { width: 1200px; height: 2601px; overflow: hidden; background: var(--bg-top); }
  body { font-family: "Plus Jakarta Sans", sans-serif; }
  .screen {
    width: 430px; height: 932px; position: relative;
    transform: scale(2.7907); transform-origin: 0 0;
    background: var(--bg-top); overflow: hidden;
  }
  .header-date {
    position: absolute; left: 38px; top: 62px;
    font-size: 27px; font-weight: 800; color: var(--plum); letter-spacing: -0.2px;
  }
  .avatar {
    position: absolute; left: 339px; top: 52px; width: 57px; height: 57px;
    border-radius: 50%; background: radial-gradient(circle at 50% 60%, #f3c59a 0 38%, var(--avatar) 40%);
  }
  .intake-card {
    position: absolute; left: 0; top: 160px; width: 430px; height: 800px;
    background: var(--card); border-radius: 30px 30px 0 0;
  }
  .intake-title {
    position: absolute; top: 205px; width: 100%; text-align: center;
    font-size: 23px; font-weight: 500; color: var(--plum);
  }
  .milk-bottle-art {
    position: absolute; left: 45px; top: 286px; width: 113px; height: 331px;
    border-radius: 40px 40px 14px 14px;
    background: linear-gradient(180deg, #fcc98a 0%, #a9b2f6 22%, #eed9fc 32%, #eed9fc 62%, #ffffff 64%, #eedcfb 100%);
  }
  .water-bottle-art {
    position: absolute; left: 255px; top: 399px; width: 77px; height: 211px;
    border-radius: 14px 14px 10px 10px;
    background: linear-gradient(180deg, #9fb4f6 0%, #eed9fc 20%, #a2e4f8 30%, #e9f8fd 100%);
  }
  .gauges { position: absolute; left: 0; top: 0; }
  .gauge-label {
    position: absolute; top: 640px; font-size: 17px; font-weight: 700; color: var(--ink);
    transform: translateX(-50%);
  }
  .gauge-label.milk { left: 102px; }
  .gauge-label.water { left: 294px; }
  .control-panel {
    position: absolute; left: 0; top: 720px; width: 430px; height: 240px;
    background: var(--panel); border-radius: 30px 30px 0 0;
  }
  .step-btn {
    position: absolute; top: 755px; width: 60px; height: 60px; border-radius: 50%;
    border: 2px solid var(--plum); background: none;
  }
  .step-btn.minus { left: 36px; }
  .step-btn.plus { left: 335px; }
  .step-btn::before, .step-btn.plus::after {
    content: ""; position: absolute; left: 50%; top: 50%; width: 20px; height: 2px;
    background: var(--plum); transform: translate(-50%, -50%);
  }
  .step-btn.plus::after { width: 2px; height: 20px; }
  .burp-count {
    position: absolute; top: 770px; width: 100%; text-align: center;
    font-size: 23px; font-weight: 700; color: var(--plum);
  }
  .next-intake {
    position: absolute; left: 36px; top: 842px; width: 358px; height: 55px;
    border: 1.5px solid var(--ink); border-radius: 12px;
    display: flex; align-items: center; justify-content: center;
    font-size: 16px; font-weight: 500; color: var(--ink);
  }
</style>
</head>
<body>
<main class="screen">
  <div class="header-date">16 Sept 2023</div>
  <div class="avatar" role="img" aria-label="Baby profile illustration"></div>

  <section class="intake-card"></section>
  <h1 class="intake-title">Milo’s intake today</h1>

  <div class="milk-bottle-art" role="img" aria-label="Illustrated baby bottle filled to 150 ml of milk"></div>
  <div class="water-bottle-art" role="img" aria-label="Illustrated water bottle filled to 170 ml"></div>

  <svg class="gauges" width="430" height="720" viewBox="0 0 430 720" aria-hidden="true">
    <path d="M180 389V609" stroke="var(--rule)" stroke-width="1.5"/>
    <path d="M180 391h20M180 405h20M180 419h20M180 433h20M180 447h20M180 461h20M180 475h20M180 489h20M180 503h20M180 517h20M180 531h20M180 545h20M180 559h20M180 573h20M180 587h20M180 601h20"
          stroke="var(--rule)" stroke-width="1.3"/>
    <path d="M166 495 L173 485 H219 V507 H173 Z" fill="var(--tag)" stroke="var(--rule)" stroke-width="1"/>
    <text x="196" y="499.5" text-anchor="middle" font-family="Plus Jakarta Sans, sans-serif" font-size="10.5" font-weight="600" fill="#2e2436">150 ml</text>

    <path d="M352 391V605" stroke="var(--rule)" stroke-width="1.5"/>
    <path d="M352 393h21M352 407h21M352 421h21M352 435h21M352 449h21M352 463h21M352 477h21M352 491h21M352 504h21M352 518h21M352 532h21M352 546h21M352 560h21M352 574h21M352 588h21M352 602h21"
          stroke="var(--rule)" stroke-width="1.3"/>
    <path d="M340 455 L347 444 H392 V467 H347 Z" fill="var(--tag)" stroke="var(--rule)" stroke-width="1"/>
    <text x="369" y="459.5" text-anchor="middle" font-family="Plus Jakarta Sans, sans-serif" font-size="10.5" font-weight="600" fill="#2e2436">170 ml</text>
  </svg>

  <div class="gauge-label milk">MILK</div>
  <div class="gauge-label water">WATER</div>

  <section class="control-panel"></section>
  <button class="step-btn minus" aria-label="Remove burp"></button>
  <div class="burp-count">2 times burped</div>
  <button class="step-btn plus" aria-label="Add burp"></button>
  <div class="next-intake">2 hours left for next intake</div>
</main>
</body>
</html>
```